Single Graphical Representation of our offering

We want to have a single graphical representation of our product technology offering. We offer a series of solutions within our 'enterprise' framework. The included PPT has a simplistic representation of what we are trying to present. This would be included in PPT presentations and possibly website.

```html
<!DOCTYPE html>
<html lang="en">
<head>
<meta charset="utf-8">
<title>Keystone Solutions Overview</title>
<link href="https://fonts.googleapis.com/css2?family=Montserrat:wght@400;500;600;700;800&family=Big+Shoulders+Display:wght@800&display=swap" rel="stylesheet">
<style>
  :root{
    --slate:#546b79; --slate-2:#5b7280;
    --blue:#3574b6; --blue-2:#3f9ac6;
    --amber:#f6a400; --amber-2:#f7a800;
    --lilac:#8ea5dd; --lilac-2:#93b0e8;
    --teal:#33a79b; --teal-2:#3aafa3;
    --red:#e8202a; --ink:#3a4552; --text:#1f2329; --muted:#4d5560;
  }
  *{box-sizing:border-box;margin:0;padding:0}
  html,body{width:694px;height:1200px;overflow:hidden;background:#fff}
  body{position:relative;font-family:"Montserrat",sans-serif;color:var(--text)}
  .panel{position:absolute;left:31px;width:620px;background:linear-gradient(135deg,#f8f8f9 0%,#eceef0 60%,#e3e6ea 100%)}
  .panel--list{top:38px;height:548px}
  .panel--overview{top:602px;height:548px}
  .row{position:absolute;}
  .band{position:absolute;left:0;top:0;height:100%}
  .num{position:absolute;font-family:"Big Shoulders Display",sans-serif;font-weight:800;color:#fff;line-height:1;letter-spacing:-1px}
  .card{position:absolute;background:#fff;border-radius:40px 7px 7px 40px;box-shadow:0 2px 5px rgba(0,0,0,.22);display:flex;align-items:center}
  .card__text{flex:1}
  .card__title{font-weight:700;text-transform:uppercase;line-height:1}
  .card__body{font-weight:500;color:var(--text);line-height:1.25}
  .card__icon{flex:none}
  .ops .band{background:var(--slate)} .ops .card__title{color:var(--slate)}
  .ore .band{background:linear-gradient(90deg,var(--blue),var(--blue-2))} .ore .card__title{color:var(--blue)}
  .ent .band{background:var(--amber)} .ent .card__title{color:var(--amber)}
  .ana .band{background:linear-gradient(90deg,var(--lilac),var(--lilac-2))} .ana .card__title{color:var(--lilac)}
  .biz .band{background:var(--teal)} .biz .card__title{color:var(--teal)}

  /* large list */
  .panel--list .row{left:36px;width:584px;height:80px}
  .panel--list .band{width:529px}
  .panel--list .num{left:12px;top:15px;font-size:58px}
  .panel--list .card{left:130px;top:8px;width:418px;height:64px;padding:0 8px 0 29px}
  .panel--list .card__title{font-size:15px;margin-bottom:6px}
  .panel--list .card__body{font-size:8px}
  .panel--list .card__icon{width:46px;height:46px}

  /* overview list */
  .overview__title{position:absolute;left:38px;top:622px;font-size:38px;font-weight:700;color:var(--ink);letter-spacing:-.3px;line-height:1}
  .overview__sub{position:absolute;left:38px;top:668px;font-size:17.5px;font-weight:600;color:#15181c;letter-spacing:-.2px}
  .overview__sub em{font-style:normal;color:var(--red)}
  .overview__intro{position:absolute;left:38px;top:704px;width:580px;font-size:10.6px;line-height:1.18;color:var(--muted)}
  .panel--overview .row{left:38px;width:460px;height:67px}
  .panel--overview .band{width:443px}
  .panel--overview .num{left:10px;top:12px;font-size:48px}
  .panel--overview .card{left:108px;top:7px;width:351px;height:53px;padding:0 8px 0 24px}
  .panel--overview .card__title{font-size:13px;margin-bottom:5px}
  .panel--overview .card__body{font-size:6.6px}
  .panel--overview .card__icon{width:38px;height:38px}
</style>
</head>
<body>
<svg width="0" height="0" style="position:absolute" aria-hidden="true">
  <defs>
    <symbol id="i-target" viewBox="0 0 48 48">
      <circle cx="22" cy="26" r="19" fill="#4e6472"/>
      <circle cx="22" cy="26" r="14" fill="#fff"/>
      <circle cx="22" cy="26" r="10.5" fill="#e8202a"/>
      <circle cx="22" cy="26" r="6" fill="#fff"/>
      <circle cx="22" cy="26" r="2.5" fill="#e8202a"/>
      <path d="M22 26 L42 6" stroke="#4e6472" stroke-width="2.4" stroke-linecap="round"/>
      <path d="M38 5 l6 -3 -2 6 z M41 4 l5 1 -4 3z" fill="#e8202a"/>
    </symbol>
    <symbol id="i-ledger" viewBox="0 0 48 48">
      <path d="M3 3 h26 l6 6 v34 h-32z" fill="#fff" stroke="#3574b6" stroke-width="2"/>
      <g stroke="#e8202a" stroke-width="2"><path d="M8 12h16M8 17h18M8 22h16M8 27h14M8 32h14M8 37h14"/></g>
      <rect x="25" y="22" width="19" height="24" rx="2" fill="#fff" stroke="#3574b6" stroke-width="2"/>
      <rect x="28" y="25" width="13" height="6" fill="none" stroke="#e8202a" stroke-width="1.6"/>
      <g fill="#3574b6"><rect x="28" y="34" width="3" height="2"/><rect x="33" y="34" width="3" height="2"/><rect x="38" y="34" width="3" height="2"/><rect x="28" y="38" width="3" height="2"/><rect x="33" y="38" width="3" height="2"/><rect x="38" y="38" width="3" height="2"/><rect x="28" y="42" width="3" height="2"/><rect x="33" y="42" width="3" height="2"/><rect x="38" y="42" width="3" height="2"/></g>
    </symbol>
    <symbol id="i-network" viewBox="0 0 48 48">
      <g stroke="#f6a400" stroke-width="2.6"><path d="M22 24 L8 12 M22 24 L40 9 M22 24 L42 28 M22 24 L27 38 M22 24 L8 40"/></g>
      <g fill="#f6a400"><circle cx="8" cy="12" r="4"/><circle cx="40" cy="9" r="4.5"/><circle cx="42" cy="28" r="3"/><circle cx="27" cy="38" r="4"/><circle cx="8" cy="40" r="4"/></g>
      <circle cx="22" cy="24" r="5.5" fill="#e8202a"/>
    </symbol>
    <symbol id="i-analysis" viewBox="0 0 48 48">
      <circle cx="19" cy="22" r="14" fill="#fff" stroke="#8ea5dd" stroke-width="4"/>
      <path d="M28 32 l12 12" stroke="#8ea5dd" stroke-width="6" stroke-linecap="round"/>
      <g fill="#e8202a"><rect x="11" y="13" width="3" height="16"/><rect x="15" y="18" width="3" height="11"/><rect x="19" y="21" width="3" height="8"/><rect x="23" y="24" width="3" height="5"/></g>
      <path d="M38 4 a7 7 0 1 0 7 7 h-7z" fill="#8ea5dd"/>
      <path d="M40 2 a7 7 0 0 1 7 7 h-7z" fill="#e8202a"/>
    </symbol>
    <symbol id="i-growth" viewBox="0 0 48 48">
      <g fill="#33a79b"><rect x="6" y="32" width="5" height="13"/><rect x="15" y="26" width="5" height="19"/><rect x="24" y="32" width="5" height="13"/><rect x="33" y="24" width="5" height="21"/></g>
      <path d="M3 26 L14 15 L23 23 L39 8" fill="none" stroke="#e8202a" stroke-width="4" stroke-linejoin="round"/>
      <path d="M33 5 l11 -2 -2 11z" fill="#e8202a"/>
    </symbol>
  </defs>
</svg>

<section class="panel panel--list">
  <div class="row ops" style="top:57px"><div class="band"></div><div class="num">01</div>
    <div class="card"><div class="card__text"><h3 class="card__title">Keystone Ops</h3><p class="card__body">Collect and understand key operating metrics, &nbsp;monitor performance-to-plan,<br>empower SIC and understand what is driving your business.</p></div><svg class="card__icon" role="img" aria-label="Target icon"><use href="#i-target"/></svg></div></div>
  <div class="row ore" style="top:145px"><div class="band"></div><div class="num">02</div>
    <div class="card"><div class="card__text"><h3 class="card__title">Ore Accounting</h3><p class="card__body">Clear visibility of your production and commodities from model to market with<br>full value chain reconciliation.</p></div><svg class="card__icon" role="img" aria-label="Ledger and calculator icon"><use href="#i-ledger"/></svg></div></div>
  <div class="row ent" style="top:234px"><div class="band"></div><div class="num">03</div>
    <div class="card"><div class="card__text"><h3 class="card__title">Keystone Enterprises</h3><p class="card__body">Integrate systems, optimize data management, and connect people through a<br>single, unified, and verifiable view of your mining enterprise.</p></div><svg class="card__icon" role="img" aria-label="Network icon"><use href="#i-network"/></svg></div></div>
  <div class="row ana" style="top:322px"><div class="band"></div><div class="num">04</div>
    <div class="card"><div class="card__text"><h3 class="card__title">Keystone Analysis</h3><p class="card__body">Powerful reporting, visualization, analytics and notifications for the operation or<br>the entire enterprise.</p></div><svg class="card__icon" role="img" aria-label="Analytics magnifier icon"><use href="#i-analysis"/></svg></div></div>
  <div class="row biz" style="top:410px"><div class="band"></div><div class="num">05</div>
    <div class="card"><div class="card__text"><h3 class="card__title">Breadth of the Business</h3><p class="card__body">Integrate operational (FMS, PCS, ERP) with operational metrics for a broad<br>reaching understanding of business performance.</p></div><svg class="card__icon" role="img" aria-label="Growth chart icon"><use href="#i-growth"/></svg></div></div>
</section>

<section class="panel panel--overview">
  <div class="row ops" style="top:156px"><div class="band"></div><div class="num">01</div>
    <div class="card"><div class="card__text"><h3 class="card__title">Keystone Ops</h3><p class="card__body">Collect and understand key operating metrics, &nbsp;monitor performance-to-plan,<br>empower SIC and understand what is driving your business.</p></div><svg class="card__icon" role="img" aria-label="Target icon"><use href="#i-target"/></svg></div></div>
  <div class="row ore" style="top:230px"><div class="band"></div><div class="num">02</div>
    <div class="card"><div class="card__text"><h3 class="card__title">Ore Accounting</h3><p class="card__body">Clear visibility of your production and commodities from model to market with<br>full value chain reconciliation.</p></div><svg class="card__icon" role="img" aria-label="Ledger and calculator icon"><use href="#i-ledger"/></svg></div></div>
  <div class="row ent" style="top:304px"><div class="band"></div><div class="num">03</div>
    <div class="card"><div class="card__text"><h3 class="card__title">Keystone Enterprises</h3><p class="card__body">Integrate systems, optimize data management, and connect people through a<br>single, unified, and verifiable view of your mining enterprise.</p></div><svg class="card__icon" role="img" aria-label="Network icon"><use href="#i-network"/></svg></div></div>
  <div class="row ana" style="top:378px"><div class="band"></div><div class="num">04</div>
    <div class="card"><div class="card__text"><h3 class="card__title">Keystone Analysis</h3><p class="card__body">Powerful reporting, visualization, analytics and notifications for the operation or<br>the entire enterprise.</p></div><svg class="card__icon" role="img" aria-label="Analytics magnifier icon"><use href="#i-analysis"/></svg></div></div>
  <div class="row biz" style="top:452px"><div class="band"></div><div class="num">05</div>
    <div class="card"><div class="card__text"><h3 class="card__title">Breadth of the Business</h3><p class="card__body">Integrate operational (FMS, PCS, ERP) with operational metrics for a broad<br>reaching understanding of business performance.</p></div><svg class="card__icon" role="img" aria-label="Growth chart icon"><use href="#i-growth"/></svg></div></div>
</section>

<h1 class="overview__title">Keystone Solutions Overview</h1>
<h2 class="overview__sub">An Integrated Platform Across the <em>Entire Mining Value Chain.</em></h2>
<p class="overview__intro">Keystone provides mining-specific solutions within an Enterprise Framework that unifies workflows, provides accountability for decision making and empowers you to ask entirely new questions of the vast quantities of data you collect.</p>
</body>
</html>
```